"Psychic / Tarot Card Reader / Healer Needs a Web Page Design

We need a web page design for company that does psychic / tarot card readings / healings etc.
It currently has 6 different tabs which include: Home, testimonials, service, certificates, contact us plus a shop where if people want to they can purchase services on line.
Should be mystical / magic like yet simple.
Will upload a copy of the current logo for the business.
It's name is Lunar Hollow.

Target Market(s)

spiritual

Industry/Entity Type

It Company

Number of Pages Required

5+ page

```html
<!DOCTYPE html>
<html lang="en">
<head>
<meta charset="utf-8">
<title>Lunar Hollow</title>
<link rel="stylesheet" href="https://fonts.googleapis.com/css2?family=Open+Sans:wght@400;600;700;800&family=Jost:wght@400;500&display=swap">
<style>
:root{
  --purple:#7a1d7c;
  --purple-light:#9a4c9c;
  --purple-mid:#8a3490;
  --ink:#3d3d3d;
  --body:#555;
  --white:#fff;
  --night:#0c1326;
}
*{margin:0;padding:0;box-sizing:border-box}
html,body{width:1200px;height:2564px;overflow:hidden;background:var(--white)}
body{font-family:"Open Sans",Arial,sans-serif;color:var(--body);position:relative}
.page{position:relative;width:1200px;height:2564px;overflow:hidden}
.abs{position:absolute}

.topbar{left:0;top:0;width:1200px;height:44px;
  background:linear-gradient(110deg,var(--purple) 0 46%,var(--purple-light) 46% 100%)}
.topbar .contact{left:103px;top:0;height:44px;display:flex;align-items:center;gap:22px;color:var(--white);font-size:12px}
.topbar .contact span{display:flex;align-items:center;gap:8px}
.topbar .social{right:90px;top:0;height:44px;display:flex;align-items:center;gap:14px}
.topbar .social i{display:block;width:9px;height:9px;border-radius:50%;background:var(--white)}

.brand{left:0;top:62px;width:1200px;text-align:center;font-family:"Jost",sans-serif;font-weight:500;font-size:38px;color:var(--purple);line-height:1;display:flex;justify-content:center;align-items:center;gap:12px}
.brand i{width:14px;height:14px;border-radius:50%;background:var(--purple);display:block}

.nav{left:0;top:174px;width:1200px;display:flex;justify-content:center;gap:0}
.nav a{color:#222;text-decoration:none;font-size:15px;font-family:"Open Sans",sans-serif;width:146px;text-align:center}

.hero{left:0;top:205px;width:1200px;height:516px;
  background:radial-gradient(ellipse at 50% 30%,#e9ece6 0%,#c9cdbd 25%,#8d8a67 55%,#4d4b33 80%,#2e2d20 100%)}
.hero h1{position:absolute;left:0;top:220px;width:1200px;text-align:center;color:var(--white);font-weight:800;font-size:52px;letter-spacing:.5px}

.welcome h2{left:101px;top:835px;font-family:"Jost",sans-serif;font-weight:400;font-size:31px;color:var(--ink)}
.welcome h3{left:103px;top:888px;font-size:19px;font-weight:600;color:var(--purple)}
.welcome p{left:103px;width:530px;font-size:12.5px;line-height:23px;color:var(--body)}
.btn{left:103px;top:1094px;width:147px;height:38px;background:var(--purple);color:var(--white);font-size:14px;font-weight:700;display:flex;align-items:center;justify-content:center;gap:10px}
.frame{left:766px;top:786px;width:318px;height:376px;border:3px solid var(--purple)}
.photo-hood{left:706px;top:810px;width:326px;height:327px;
  background:linear-gradient(160deg,#dfe5e2 0%,#aeb8b8 45%,#2b3038 75%,#4a5058 100%)}

.band{left:0;width:1200px;height:72px;display:flex;align-items:center;justify-content:center;
  background:linear-gradient(108deg,var(--purple) 0 60%,var(--purple-light) 60% 100%)}
.band h2{font-family:"Jost",sans-serif;font-weight:400;font-size:30px;color:var(--white)}

.chakra{left:154px;top:1359px;width:376px;height:307px;
  background:radial-gradient(ellipse at 50% 55%,#f2a03a 0%,#e5483a 35%,#5da0d6 60%,rgba(255,255,255,0) 75%)}
.service h3{left:578px;top:1372px;font-family:"Jost",sans-serif;font-weight:400;font-size:31px;color:var(--purple)}
.service p{left:578px;width:502px;font-size:12px;line-height:22px;color:var(--body);text-align:justify}
.dots{left:1134px;top:1494px;display:flex;flex-direction:column;gap:13px}
.dots i{display:block;width:13px;height:13px;border-radius:50%;border:2px solid var(--purple)}

.product{top:1882px;height:318px}
.cover-angel{background:linear-gradient(180deg,#8ec9ea 0%,#3d7fbf 30%,#2d6a3a 60%,#2f5d9b 100%);border:2px solid #5aa3d6}
.cover-chakra{background:radial-gradient(ellipse at 50% 50%,#3b5aa8 0%,#1a2450 45%,#05070f 100%)}
.cover-dream{background:linear-gradient(180deg,#0e1730,var(--night));color:var(--white);text-align:center;font-family:"Jost",sans-serif}
.cover-dream .t{margin-top:75px;font-size:31px;line-height:38px}
.cover-dream .p{margin-top:16px;font-size:31px}
.cover-dream .b{margin-top:16px;font-size:19px;text-decoration:underline}

.footer{left:0;top:2265px;width:1200px;height:299px;
  background:linear-gradient(110deg,var(--purple-light) 0 48%,var(--purple) 48% 100%)}
.footer .brand{top:90px;color:var(--white);font-size:54px}
.footer .brand i{background:var(--white);width:18px;height:18px}
.footer .fnav{position:absolute;left:0;top:222px;width:1200px;display:flex;justify-content:center;gap:46px}
.footer .fnav a{color:var(--white);font-size:13px;text-decoration:none}
.footer .copy{position:absolute;left:0;top:262px;width:1200px;text-align:center;color:var(--white);font-size:11.5px}
</style>
</head>
<body>
<div class="page">

  <header>
    <div class="abs topbar">
      <div class="abs contact">
        <span><svg width="11" height="11" viewBox="0 0 12 12"><rect width="12" height="12" rx="2" fill="#fff"/><path d="M3.5 2.5l1.5 0 .7 2-1 .8a5 5 0 0 0 2 2l.8-1 2 .7v1.5c0 .5-.5 1-1 1A6.5 6.5 0 0 1 2.5 3.5c0-.5.5-1 1-1z" fill="#7a1d7c"/></svg>0400 555 273</span>
        <span><svg width="12" height="9" viewBox="0 0 12 9"><rect width="12" height="9" fill="#fff"/><path d="M0 0l6 5 6-5" stroke="#7a1d7c" fill="none"/></svg>hello@lunarhollow.example</span>
      </div>
      <div class="abs social"><i></i><i></i><i></i></div>
    </div>
    <div class="abs brand"><i></i>Lunar Hollow</div>
    <nav class="abs nav">
      <a>Home</a><a>Testimonials</a><a>Service</a><a>Certificates</a><a>Contact</a><a>Shop</a>
    </nav>
  </header>

  <section class="abs hero" role="img" aria-label="Photo of two open hands reaching upward into soft glowing light">
    <h1>MAKE YOUR WORLD EASY WITH US</h1>
  </section>

  <section class="welcome">
    <h2 class="abs">Welcome To Lunar Hollow</h2>
    <h3 class="abs">Aim To Get Positive Outcome</h3>
    <p class="abs" style="top:932px">Maren has undertaken various training courses to give herself an indepth knowledge and understanding of Tarot and Reiki whilst applying her intution to provide her clients with indepth readings. She aims to offer clients guidance and support in any area of their life through the use of these methods.</p>
    <p class="abs" style="top:1022px">When providing Readings and Reiki Healings, Maren will use her skills and intuition to pass on accurate messages to clients from Heavenly Beings who wish their words and advice to become heard.</p>
    <div class="abs btn">Read More
      <svg width="13" height="13" viewBox="0 0 13 13"><circle cx="6.5" cy="6.5" r="5.5" fill="none" stroke="#fff" stroke-width="1.6"/><path d="M5 4l2.5 2.5L5 9" fill="none" stroke="#fff" stroke-width="1.6"/></svg>
    </div>
    <div class="abs frame"></div>
    <div class="abs photo-hood" role="img" aria-label="Photo of a hooded figure holding out one hand against a misty sky"></div>
  </section>

  <div class="abs band" style="top:1237px"><h2>Our Services</h2></div>

  <section class="service">
    <div class="abs chakra" role="img" aria-label="Watercolour illustration of a meditating figure with seven chakra symbols"></div>
    <h3 class="abs">Reiki Healings</h3>
    <p class="abs" style="top:1428px">Reiki is a healing techique that uses the energy of the universe to heal your mind, body or spirit. It enhances the natural healing ability and is completely safe and is also an effective way of unblocking our chakras.</p>
    <p class="abs" style="top:1512px">When receiving a Reiki Healing, the healing energy will flow to whichever areas of the body need it at that time. It is channeled through the person performing the healing and passed out through their hands to the client.</p>
    <p class="abs" style="top:1596px">As a Reiki Master trained in the Japanese Usui method, I can help! Reiki can either be in person or sent via distance and both are just as effective. Not only can Reiki be sent to a person but can be sent to any situation.</p>
    <div class="abs dots"><i></i><i></i><i></i><i></i></div>
  </section>

  <div class="abs band" style="top:1738px"><h2>Shop Now</h2></div>

  <section class="shop">
    <div class="abs product cover-angel" style="left:85px;width:224px" role="img" aria-label="Tarot card deck box cover with an angel artwork"></div>
    <div class="abs product cover-chakra" style="left:338px;width:231px" role="img" aria-label="Illustration of a glowing meditating figure with chakras on a starry background"></div>
    <div class="abs product cover-angel" style="left:629px;width:231px" role="img" aria-label="Tarot card deck box cover with an angel artwork"></div>
    <div class="abs product cover-dream" style="left:894px;width:222px">
      <div class="t">Dream<br>Interpretation</div>
      <div class="p">AU$45.00</div>
      <div class="b">BUY NOW</div>
    </div>
  </section>

  <footer class="abs footer">
    <div class="abs brand"><i></i>Lunar Hollow</div>
    <nav class="fnav"><a>Home</a><a>Services</a><a>Testimonials</a><a>Shop</a><a>Certificates</a><a>Contact Us</a></nav>
    <div class="copy">Copyright 2017 Lunar Hollow. All Rights Reserved.</div>
  </footer>

</div>
</body>
</html>
```